Mobile Game identical to "Letter Orbit"

We need a design for mobile game identical to "Letter Orbit" you can get from app store using this link https://quickstorelink.example/us/tzvnR.k
playstore link: https://apps.samplemarket.example/store/apps/details?id=se.fenwoodgames.letterorbit&hl=en

- App name will be : Tangle
- For iOS and Android
- Same Letter Orbit features exactly but in different design.
- Ads banner will be overall app screens
- Some kind of animation is needed in the game , designer has to provide.

Requirements
Must have
• - Same Letter Orbit Features and steps
• - Some Animation
• - Game will be in arabic i will help to provide needed text

```html
<!DOCTYPE html>
<html lang="en">
<head>
<meta charset="utf-8">
<title>Tangle – Level Screen</title>
<link rel="stylesheet" href="https://fonts.googleapis.com/css2?family=Arimo:wght@400;700&family=Oswald:wght@500;600&family=Fredoka:wght@600&display=swap">
<style>
  :root {
    --page: #ffffff;
    --header-wood: #e6d2aa;
    --header-wood-dark: #d9c194;
    --ink-dark: #2f2f2f;
    --title: #4fb3c9;
    --frame-wood: #c9955c;
    --board-edge: #b65a22;
    --board: #3b3b3b;
    --tile: #fbf4e4;
    --tile-on: #f3cf98;
    --tile-letter: #3a3a3a;
    --chalk: #3e6b2b;
    --chalk-light: #4b7a34;
    --chalk-ink: #f4f4ee;
    --banner: #c98a4a;
    --banner-sky: #e9c27a;
  }
  * { box-sizing: border-box; margin: 0; padding: 0; }
  html, body { width: 683px; height: 1200px; overflow: hidden; background: var(--page); }
  .screen { width: 683px; height: 1200px; display: flex; flex-direction: column; font-family: "Arimo", Arial, sans-serif; }

  .top-bar {
    height: 112px; background: linear-gradient(180deg, var(--header-wood), var(--header-wood-dark));
    display: flex; align-items: center; justify-content: space-between; padding: 0 26px;
    border-bottom: 3px solid #bda57a;
  }
  .back-button { width: 60px; height: 44px; }
  .app-title { font-family: "Fredoka", sans-serif; font-weight: 600; font-size: 58px; color: var(--title); letter-spacing: 2px; }
  .level-code { width: 110px; text-align: right; font-family: "Oswald", sans-serif; font-weight: 600; font-size: 26px; color: var(--ink-dark); }

  .board-frame { height: 724px; background: var(--frame-wood); padding: 14px 14px 20px; }
  .board {
    height: 100%; background: var(--board); border: 8px solid var(--board-edge);
    padding: 24px 26px 0; display: flex; flex-direction: column;
  }
  .letter-grid { display: grid; grid-template-columns: repeat(5, 1fr); gap: 14px; }
  .tile {
    height: 110px; background: var(--tile); border-radius: 10px;
    display: flex; align-items: center; justify-content: center;
    font-size: 70px; color: var(--tile-letter); box-shadow: inset 0 -4px 0 rgba(0,0,0,.08);
  }
  .tile.is-selected { background: var(--tile-on); }
  .found-stat {
    margin-top: 22px; text-align: center; color: #ffffff;
    font-family: "Oswald", sans-serif; font-weight: 500; font-size: 25px; letter-spacing: .5px;
  }

  .chalkboard {
    height: 260px; background: radial-gradient(ellipse at 50% 40%, var(--chalk-light), var(--chalk));
    padding: 22px 40px 0; color: var(--chalk-ink); position: relative;
  }
  .word-row { display: flex; gap: 40px; justify-content: center; }
  .word-slot { display: flex; align-items: baseline; gap: 8px; font-family: "Arimo", sans-serif; font-weight: 700; }
  .slot-number {
    width: 26px; height: 26px; border-radius: 50%; border: 2px solid var(--chalk-ink);
    font-size: 16px; display: flex; align-items: center; justify-content: center;
  }
  .slot-letters { font-size: 30px; letter-spacing: 10px; }
  .word-row + .word-row { margin-top: 14px; }
  .controls { position: absolute; left: 40px; right: 40px; bottom: 34px; display: flex; gap: 26px; justify-content: center; }
  .control-button {
    height: 62px; border: 3px solid var(--chalk-ink); border-radius: 12px; color: var(--chalk-ink);
    display: flex; align-items: center; justify-content: center; gap: 10px;
    font-family: "Oswald", sans-serif; font-weight: 500; font-size: 26px; padding: 0 24px;
  }
  .control-button.shuffle { width: 96px; padding: 0; }

  .ad-banner { flex: 1; background: linear-gradient(180deg, var(--banner-sky), var(--banner)); }
</style>
</head>
<body>
<div class="screen">
  <header class="top-bar">
    <svg class="back-button" viewBox="0 0 60 44" aria-label="Back">
      <path d="M6 22 H54 M6 22 L22 8 M6 22 L22 36 M14 15 H54 M14 29 H54" stroke="var(--ink-dark)" stroke-width="4" fill="none" stroke-linecap="round"/>
    </svg>
    <div class="app-title">Tangle</div>
    <div class="level-code">SNAIL-7</div>
  </header>

  <section class="board-frame">
    <div class="board">
      <div class="letter-grid">
        <div class="tile is-selected">C</div><div class="tile">A</div><div class="tile">S</div><div class="tile">N</div><div class="tile">B</div>
        <div class="tile">L</div><div class="tile is-selected">O</div><div class="tile">D</div><div class="tile">U</div><div class="tile">L</div>
        <div class="tile">O</div><div class="tile is-selected">L</div><div class="tile">F</div><div class="tile">I</div><div class="tile">W</div>
        <div class="tile">C</div><div class="tile">B</div><div class="tile is-selected">O</div><div class="tile">Z</div><div class="tile">S</div>
        <div class="tile">H</div><div class="tile">S</div><div class="tile">K</div><div class="tile is-selected">R</div><div class="tile">Q</div>
      </div>
      <p class="found-stat">FOUND BY 98.01% OF PLAYERS</p>
    </div>
  </section>

  <section class="chalkboard">
    <div class="word-row">
      <div class="word-slot"><span class="slot-number">1</span><span class="slot-letters">COLOR</span></div>
      <div class="word-slot"><span class="slot-number">2</span><span class="slot-letters">______</span></div>
    </div>
    <div class="word-row">
      <div class="word-slot"><span class="slot-number">3</span><span class="slot-letters">______</span></div>
    </div>
    <div class="controls">
      <div class="control-button">? HELP</div>
      <div class="control-button shuffle">
        <svg width="40" height="34" viewBox="0 0 40 34" aria-label="Shuffle">
          <path d="M8 16 A12 12 0 0 1 30 10 M32 18 A12 12 0 0 1 10 24" stroke="var(--chalk-ink)" stroke-width="3.5" fill="none"/>
          <path d="M30 3 L31 11 L23 11 Z M10 31 L9 23 L17 23 Z" fill="var(--chalk-ink)"/>
        </svg>
      </div>
      <div class="control-button">
        <svg width="22" height="30" viewBox="0 0 22 30" aria-hidden="true">
          <path d="M11 2 A9 9 0 0 0 6 19 V23 H16 V19 A9 9 0 0 0 11 2 Z" fill="var(--chalk-ink)"/>
          <rect x="7" y="25" width="8" height="3" fill="var(--chalk-ink)"/>
        </svg>
        HINT! (20)
      </div>
    </div>
  </section>

  <div class="ad-banner" role="img" aria-label="Advertising banner with a colourful game illustration"></div>
</div>
</body>
</html>
```